Building quality affordable homes in Brisbane, Australia for investors and families

We design, build and market our own homes from small single story to large 3 story luxury homes. Our main focus is "duel key" - that is two houses on one lot - a "gribby" (as in where The Gribbs lived) or attached granny flat.
We have a logo design and need a business card to suit. Something simple but eye catching. We want to communicate: "you are making a smart financial choice buying or building with us".
Unfortunately a lot of information has to be on the card including - Name, position, phone, mobile, fax, email, web address and of course the logo.
Logo in multiple formats and high res now available.

Target Market(s)

Families, contractors, real estate agents, other builders, developers, banks and home buyers.

Industry/Entity Type

Financial

Contact Information for Business Card

Name, position, phone, mobile, fax, email, web address

Font styles to use
Serif

Requirements
Must have
• The logo, and the details.
Nice to have
• Show or explain what we do - design, build and market affordable homes.
Should not have
• Nothing too fancy, outrageous - building companies are normally very straight.

```html
<!DOCTYPE html>
<html lang="en">
<head>
<meta charset="utf-8">
<title>Keystone Dwellings – Business Card</title>
<link rel="stylesheet" href="https://fonts.googleapis.com/css2?family=Open+Sans:wght@400;600;700&display=swap">
<style>
  :root {
    --stage: #b4b4b4;
    --brand-blue: #025a96;
    --accent-blue: #0a72bd;
    --soft-blue: #7ba7dc;
    --card-white: #ffffff;
    --ink: #333333;
    --ink-muted: #444444;
  }
  * { box-sizing: border-box; margin: 0; padding: 0; }
  html, body {
    width: 1200px; height: 688px; overflow: hidden;
    background: var(--stage);
    font-family: "Open Sans", Arial, sans-serif;
  }
  .canvas { position: relative; width: 1200px; height: 688px; }

  .card {
    position: absolute; top: 175px;
    width: 553px; height: 331px;
    border-radius: 18px; overflow: hidden;
  }

  /* Front */
  .card-front { left: 28px; background: var(--brand-blue); color: var(--card-white); }
  .front-brand {
    position: absolute; right: 20px; top: 206px;
    text-align: right; font-weight: 700; color: var(--card-white);
  }
  .front-brand .brand-main { font-size: 46px; line-height: 48px; letter-spacing: -1px; }
  .front-brand .brand-sub { font-size: 17px; line-height: 22px; letter-spacing: 1px; }
  .front-tagline {
    position: absolute; right: 20px; top: 284px;
    font-size: 14.5px; font-weight: 600; letter-spacing: 1.6px;
  }

  /* Back */
  .card-back { left: 613px; background: var(--card-white); }
  .back-web {
    position: absolute; right: 22px; top: 13px;
    font-size: 14px; font-weight: 700; color: var(--accent-blue);
  }
  .back-logo { position: absolute; left: 27px; top: 22px; display: flex; align-items: center; gap: 9px; }
  .back-logo .logo-square { width: 88px; height: 88px; background: var(--soft-blue); }
  .back-logo .logo-name { font-weight: 700; color: var(--accent-blue); }
  .back-logo .brand-main { font-size: 32px; line-height: 36px; letter-spacing: -0.5px; }
  .back-logo .brand-sub { font-size: 13px; line-height: 16px; letter-spacing: 0.5px; }

  .holder { position: absolute; left: 27px; top: 142px; }
  .holder-name { font-size: 20px; font-weight: 700; color: var(--accent-blue); line-height: 26px; }
  .holder-role { font-size: 14.5px; color: var(--ink); line-height: 20px; }
  .holder-rule {
    position: absolute; left: 0; top: 194px;
    width: 278px; height: 2px; background: var(--accent-blue);
  }

  .contact-list { position: absolute; left: 27px; top: 207px; list-style: none; }
  .contact-list li {
    display: flex; align-items: center; gap: 8px;
    height: 21px; font-size: 14.5px; color: var(--ink);
  }
  .contact-list svg { width: 12px; height: 12px; flex: none; }

  .address {
    position: absolute; left: 27px; top: 299px;
    font-size: 14.5px; font-weight: 700; color: var(--ink-muted);
  }
</style>
</head>
<body>
<main class="canvas">

  <section class="card card-front" aria-label="Card front">
    <div class="front-brand">
      <div class="brand-main">Keystone</div>
      <div class="brand-sub">DWELLINGS PTY LTD</div>
    </div>
    <div class="front-tagline">DESIGN | DEVELOP | CONSTRUCT</div>
  </section>

  <section class="card card-back" aria-label="Card back">
    <div class="back-web">www.kdbrisbane.com.au</div>

    <div class="back-logo">
      <div class="logo-square"></div>
      <div class="logo-name">
        <div class="brand-main">Keystone</div>
        <div class="brand-sub">DWELLINGS PTY LTD</div>
      </div>
    </div>

    <div class="holder">
      <div class="holder-name">Marcus Hale</div>
      <div class="holder-role">Director</div>
    </div>
    <div class="holder-rule" style="left:27px"></div>

    <ul class="contact-list">
      <li>
        <svg viewBox="0 0 12 12" aria-label="Mobile"><rect width="12" height="12" rx="2" fill="#0a72bd"/><rect x="3.5" y="1.8" width="5" height="8.4" rx="1" fill="#fff"/><rect x="4.5" y="3" width="3" height="5" fill="#0a72bd"/></svg>
        0412 555 018
      </li>
      <li>
        <svg viewBox="0 0 12 12" aria-label="Phone"><rect width="12" height="12" rx="2" fill="#0a72bd"/><path d="M3 2.5 L4.6 2.5 L5.2 4.4 L4.3 5.1 Q5.2 6.9 6.9 7.7 L7.6 6.8 L9.5 7.4 L9.5 9 Q5 9.3 3 4.5 Z" fill="#fff"/></svg>
        07 3555 0142
      </li>
      <li>
        <svg viewBox="0 0 12 12" aria-label="Fax"><rect width="12" height="12" rx="2" fill="#0a72bd"/><rect x="3.5" y="2" width="5" height="3" fill="#fff"/><rect x="2" y="5" width="8" height="3.5" rx="0.6" fill="#fff"/><rect x="3.5" y="7.5" width="5" height="2.5" fill="#fff" stroke="#0a72bd" stroke-width="0.6"/></svg>
        07 3555 0143
      </li>
      <li>
        <svg viewBox="0 0 12 12" aria-label="Email"><rect width="12" height="12" rx="2" fill="#0a72bd"/><rect x="2" y="3.3" width="8" height="5.4" fill="#fff"/><path d="M2 3.3 L6 6.4 L10 3.3" fill="none" stroke="#0a72bd" stroke-width="0.9"/></svg>
        marcus@kdbrisbane.com.au
      </li>
    </ul>

    <div class="address">318 HARBOUR RD, EASTVALE, QLD 4179</div>
  </section>

</main>
</body>
</html>
```